Looking for awesome business card design with attached existing logo

We are a water, mold, and fire damage restoration company called "Torvane Seco" Looking for an awesome business card that is edgy yet professional and unique. Show me what you got!

```html
<!DOCTYPE html>
<html lang="en">
<head>
<meta charset="utf-8">
<title>Torvane Seco — Business Card</title>
<link href="https://fonts.googleapis.com/css2?family=Poppins:ital,wght@0,400;0,600;1,700&display=swap" rel="stylesheet">
<style>
  :root{
    --backdrop:#e4e4e6;
    --card:#ffffff;
    --ink:#2b4554;
    --accent-red:#b81c25;
    --accent-gold:#d4952a;
    --glow:#f7eee0;
  }
  *{box-sizing:border-box;margin:0;padding:0}
  html,body{width:1200px;height:1200px;overflow:hidden}
  body{background:var(--backdrop);font-family:"Poppins",sans-serif;color:var(--ink);position:relative}
  .card{position:absolute;left:143px;width:914px;height:534px;background:var(--card);overflow:hidden;box-shadow:0 2px 8px rgba(0,0,0,.18)}
  .card--front{top:51px}
  .card--back{top:608px}
  .glow{position:absolute;border-radius:50%;background:radial-gradient(circle,var(--glow) 0%,var(--glow) 55%,rgba(247,238,224,0) 72%)}
  .card--front .glow{left:-150px;top:150px;width:560px;height:560px}
  .card--back .glow{left:-110px;top:150px;width:460px;height:460px}
  .wordmark{position:absolute;font-weight:600;font-size:46px;line-height:1;color:var(--ink);letter-spacing:1px;white-space:nowrap;transform:translateX(-50%)}
  .card--front .wordmark{left:707px;top:214px}
  .card--back .wordmark{left:691px;top:214px}
  .holder-name{position:absolute;left:58px;top:272px;font-weight:700;font-style:italic;font-size:32px;color:var(--accent-red);line-height:1}
  .holder-role{position:absolute;left:58px;top:318px;font-weight:400;font-size:24px;color:var(--accent-red);line-height:1}
  .contact{position:absolute;font-size:23px;line-height:30px;font-weight:400}
  .contact-line{display:flex;align-items:center;gap:10px;white-space:nowrap}
  .contact-line svg{width:16px;height:16px;flex:none;fill:var(--ink)}
  .contact--direct{left:56px;top:396px}
  .contact--direct .contact-line + .contact-line{margin-top:4px}
  .contact--address{left:561px;top:394px}
  .contact--address .contact-line{align-items:flex-start}
  .contact--address svg{margin-top:7px}
</style>
</head>
<body>
  <section class="card card--front">
    <div class="glow" role="img" aria-label="Soft warm sun decoration"></div>
    <div class="wordmark">Torvane Seco</div>
    <h1 class="holder-name">Marcus Ellery</h1>
    <p class="holder-role">CEO</p>
    <div class="contact contact--direct">
      <div class="contact-line">
        <svg viewBox="0 0 16 16" aria-hidden="true"><path d="M4 1.5l2.2 3-1.3 1.6c.8 1.8 2.2 3.2 4 4l1.6-1.3 3 2.2-1.2 2.3c-.4.6-1.1.9-1.8.7C6.2 12.9 3.1 9.8 2 5.5c-.2-.7.1-1.4.7-1.8z"/></svg>
        <span>+00 (0)7412 556000</span>
      </div>
      <div class="contact-line">
        <svg viewBox="0 0 16 16" aria-hidden="true"><path d="M1.5 3.5h13v1.2L8 9.2 1.5 4.7z"/><path d="M1.5 6l6.5 4.5L14.5 6v6.5h-13z"/></svg>
        <span>ellery@torvaneseco.co.uk</span>
      </div>
    </div>
    <div class="contact contact--address">
      <div class="contact-line">
        <svg viewBox="0 0 16 16" aria-hidden="true"><path d="M8 1a4 4 0 0 1 4 4c0 3-4 7-4 7S4 8 4 5a4 4 0 0 1 4-4zm0 2.3A1.7 1.7 0 1 0 8 6.7 1.7 1.7 0 0 0 8 3.3z"/><rect x="2" y="13.5" width="12" height="1.5" rx=".7"/></svg>
        <span>Third Floor, 000 Halden<br>Street London, G1B 3DD<br>England</span>
      </div>
    </div>
  </section>

  <section class="card card--back">
    <div class="glow" role="img" aria-label="Soft warm sun decoration"></div>
    <div class="wordmark">Torvane Seco</div>
  </section>
</body>
</html>
```